Landing Page Design for Adult Dating Age Verification (18+)

The objective of this task is to design a visually appealing pre-landing page for the adult dating site "Plumvelle (site: https://plumvelle.example/)" with an age verification mechanism. The pre-landing page will feature two buttons that redirect visitors to the main offer. The design should also include a footer block that includes links to the terms of use, privacy policy, and contact us pages.

Design Requirements:
Develop an age verification section prominently displayed on the pre-landing page.
Design the section to include two buttons labeled "Yes" and "No" for visitors to confirm their age.
Ensure the section is visually appealing and clearly communicates the purpose of age verification.

Visual Appeal:
Create a visually appealing design that aligns with the branding and theme of the "Plumvelle" adult dating site.
Use suitable color schemes, typography, and graphics to enhance the overall visual appeal of the pre-landing page.

Layout and Navigation:
Design an engaging and intuitive layout that encourages visitors to interact with the page and proceed to the main offer.
Ensure clear and visible navigation elements that direct visitors to the main offer or provide additional information.

Responsive Design:
Develop a responsive design that provides a seamless user experience across various devices, including desktop and mobile.
Ensure the design elements and layout adapt well to different screen sizes and resolutions.

File Formats and Assets:
Deliver the final design in PSD, AI, or Sketch format, ensuring that the files are well-organized and layered.
Include any necessary images or assets used in the design, ensuring they are of high quality and optimized for web use.

```html
<!DOCTYPE html>
<html lang="en">
<head>
<meta charset="utf-8">
<title>Plumvelle – Pre-landing</title>
<link rel="stylesheet" href="https://fonts.googleapis.com/css2?family=Playfair+Display:wght@600;700;800&family=Quicksand:wght@400;500&display=swap">
<style>
:root{
  --page:#eee9ee;
  --plum:#c9a6cc;
  --plum-deep:#b993bd;
  --lilac-btn:#d7acdb;
  --cream:#f1ece9;
  --pill:#ece0e5;
  --ink:#27202e;
  --photo:#a98aa6;
  --white:#ffffff;
}
*{margin:0;padding:0;box-sizing:border-box}
html,body{width:811px;height:1200px;overflow:hidden}
body{background:var(--page);position:relative;font-family:"Quicksand",sans-serif;color:var(--ink)}
.screen{position:absolute;width:251px;overflow:hidden;border-radius:14px}
.screen--gate{left:96px;top:62px;height:544px;background:var(--plum)}
.screen--home{left:468px;top:62px;height:1049px;background:var(--cream)}
.backdrop{position:absolute;inset:0;background:radial-gradient(ellipse at 45% 40%,#bd98bf 0%,var(--plum) 55%,#cfb0d2 100%)}
.site-header{position:absolute;left:0;right:0;top:32px;height:20px;display:flex;align-items:center;padding:0 8px}
.brand{display:flex;align-items:center;gap:5px;font-family:"Playfair Display",serif;font-weight:700;font-size:12px;color:var(--ink)}
.brand__dot{width:12px;height:12px;border-radius:50%;background:#e6d2e8}
.nav{margin-left:auto;display:flex;gap:18px;font-family:"Playfair Display",serif;font-weight:700;font-size:9.5px;letter-spacing:.4px;color:var(--ink)}
.age-card{position:absolute;left:0;top:166px;width:251px;height:134px;border-radius:67px;background:var(--pill);opacity:.95}
.age-card__q{position:absolute;left:0;right:0;top:41px;text-align:center;font-family:"Playfair Display",serif;font-weight:700;font-size:15.5px}
.btn{position:absolute;display:flex;align-items:center;justify-content:center;border-radius:14px;font-family:"Playfair Display",serif;font-weight:700;letter-spacing:.5px}
.btn--yes{left:22px;top:79px;width:98px;height:27px;background:var(--lilac-btn);color:var(--white);font-size:8px}
.btn--no{left:132px;top:79px;width:98px;height:27px;background:var(--white);color:var(--ink);font-size:8px}
.hero-shape{position:absolute;left:0;top:0}
.photo{position:absolute;border-radius:50%;background:radial-gradient(circle at 40% 35%,#c8a79a,var(--photo) 60%,#6d5464)}
.hero-card{position:absolute;left:12px;top:98px;width:225px;height:97px;border-radius:48px;background:var(--cream);text-align:center}
.hero-card__title{margin-top:14px;font-family:"Playfair Display",serif;font-weight:700;font-size:12.5px;line-height:15.5px}
.hero-card__lead{margin-top:3px;font-size:7.3px}
.hero-card .btn--join{left:28px;top:67px;width:89px;height:20px;border-radius:10px;background:var(--lilac-btn);color:var(--white);font-size:7.5px}
.hero-card .link--more{position:absolute;left:128px;top:72px;font-family:"Playfair Display",serif;font-weight:700;font-size:7.5px;letter-spacing:.4px}
.intro{position:absolute;left:40px;top:309px;width:170px;text-align:center}
.intro__title{font-family:"Playfair Display",serif;font-weight:700;font-size:12px}
.intro__text{margin-top:6px;font-size:7.2px;line-height:10.7px}
.steps__title{position:absolute;left:0;right:0;top:429px;text-align:center;font-family:"Playfair Display",serif;font-weight:800;font-size:10px;letter-spacing:.6px}
.step{position:absolute;left:0;width:251px;text-align:center;font-size:10px}
.step svg{position:absolute}
.cta__title{position:absolute;left:0;right:0;top:773px;text-align:center;font-family:"Playfair Display",serif;font-weight:800;font-size:15.5px;letter-spacing:.8px}
.cta .btn--join{left:59px;top:806px;width:131px;height:38px;border-radius:19px;background:var(--lilac-btn);color:var(--white);font-size:10px}
.footer-shape{position:absolute;left:0;top:0}
.footer__brand{position:absolute;left:9px;top:929px;font-family:"Playfair Display",serif;font-weight:700;font-size:7.5px;color:var(--white);letter-spacing:.3px}
.footer__tag{position:absolute;left:9px;top:942px;font-family:"Playfair Display",serif;font-weight:700;font-size:13px;line-height:13.5px}
.footer__rule{position:absolute;left:9px;right:8px;top:987px;height:1px;background:rgba(255,255,255,.7)}
.footer__links{position:absolute;left:9px;right:8px;top:1000px;display:flex;justify-content:space-between;font-family:"Playfair Display",serif;font-weight:700;font-size:6.5px;color:var(--white)}
.footer__url{position:absolute;left:0;right:0;top:1028px;text-align:center;font-size:6.5px;color:rgba(255,255,255,.85);letter-spacing:.3px}
</style>
</head>
<body>

<section class="screen screen--gate">
  <div class="backdrop" role="img" aria-label="Soft-focus photo of an embracing couple, tinted lilac"></div>
  <header class="site-header">
    <div class="brand"><span class="brand__dot"></span>Plumvelle</div>
    <nav class="nav"><span>SIGN IN</span><span>JOIN</span></nav>
  </header>
  <div class="age-card">
    <p class="age-card__q">Are you 18 years or older?</p>
    <a class="btn btn--yes">YES</a>
    <a class="btn btn--no">NO</a>
  </div>
</section>

<section class="screen screen--home">
  <svg class="hero-shape" width="251" height="300" viewBox="0 0 251 300" role="img" aria-label="Lilac-tinted photo of a couple behind the hero">
    <path d="M0 0H251V290C205 298 140 292 105 258C80 232 50 198 0 197Z" fill="#c6a3c9"/>
  </svg>
  <header class="site-header">
    <div class="brand"><span class="brand__dot"></span>Plumvelle</div>
    <nav class="nav"><span>SIGN IN</span><span>JOIN</span></nav>
  </header>

  <div class="photo" style="left:-2px;top:66px;width:52px;height:52px" role="img" aria-label="Portrait photo of a woman"></div>
  <div class="photo" style="left:216px;top:91px;width:27px;height:27px" role="img" aria-label="Portrait photo of a woman"></div>
  <div class="photo" style="left:210px;top:168px;width:48px;height:48px" role="img" aria-label="Portrait photo of a woman"></div>
  <div class="photo" style="left:-22px;top:206px;width:102px;height:102px" role="img" aria-label="Portrait photo of a woman"></div>
  <div class="photo" style="left:204px;top:337px;width:60px;height:60px" role="img" aria-label="Portrait photo of a woman"></div>

  <div class="hero-card">
    <h1 class="hero-card__title">Meet Your Dream Partner<br>With Plumvelle</h1>
    <p class="hero-card__lead">We will find your dream girl especially for you</p>
    <a class="btn btn--join">JOIN NOW</a>
    <a class="link--more">LEARN MORE</a>
  </div>

  <div class="intro">
    <h2 class="intro__title">The Best place to find her</h2>
    <p class="intro__text">Forget about looking through thousands of profiles every day and leave the finding to us. We will find the partner especailly suited to you and send a matching one everyday so you can start chatting right away.</p>
  </div>

  <h3 class="steps__title">SEE HOW EASY IT IS</h3>

  <div class="step" style="top:455px;height:84px">
    <svg style="left:94px;top:0" width="70" height="60" viewBox="0 0 70 60">
      <circle cx="27" cy="29" r="23" fill="#d7acdb"/>
      <path d="M26 10h26l8 8v32H26Z" fill="none" stroke="#111" stroke-width="1.6"/>
      <path d="M30 17h6v5h-6zM30 26h6v5h-6zM30 35h6v5h-6zM39 19h10M39 28h10M39 37h7" fill="none" stroke="#111" stroke-width="1.6"/>
      <path d="M47 50l2-7 14-14 5 5-14 14z" fill="var(--cream)" stroke="#111" stroke-width="1.6"/>
    </svg>
    <span style="position:absolute;left:0;right:0;top:70px">1. Fill Out The Form</span>
  </div>

  <div class="step" style="top:567px;height:70px">
    <svg style="left:104px;top:0" width="60" height="50" viewBox="0 0 60 50">
      <circle cx="34" cy="30" r="21" fill="#d7acdb"/>
      <path d="M2 6h44v32H2Z" fill="none" stroke="#111" stroke-width="1.6"/>
      <path d="M2 6l22 18 22-18M2 38l15-14M46 38L31 24" fill="none" stroke="#111" stroke-width="1.6"/>
      <path d="M22 28l4 16 3-5 5 6 3-2-5-6 5-2z" fill="var(--cream)" stroke="#111" stroke-width="1.4"/>
    </svg>
    <span style="position:absolute;left:0;right:0;top:54px">2. Confirm Your Email</span>
  </div>

  <div class="step" style="top:667px;height:76px">
    <svg style="left:94px;top:0" width="70" height="56" viewBox="0 0 70 56">
      <circle cx="24" cy="25" r="23" fill="#d7acdb"/>
      <path d="M12 12h34v26H26l-7 6v-6h-7Z" fill="none" stroke="#111" stroke-width="1.6"/>
      <path d="M17 19h24M17 25h24M17 31h14" stroke="#111" stroke-width="1.6"/>
      <path d="M46 20h6a8 8 0 0 1 8 8v4a8 8 0 0 1-6 8v6l-6-6H36" fill="none" stroke="#111" stroke-width="1.6"/>
    </svg>
    <span style="position:absolute;left:0;right:0;top:61px">3. Start Chatting</span>
  </div>

  <div class="cta">
    <h2 class="cta__title">SHE’S WAITING FOR YOU</h2>
    <a class="btn btn--join">JOIN NOW</a>
  </div>

  <footer>
    <svg class="footer-shape" width="251" height="1049" viewBox="0 0 251 1049" role="img" aria-label="Lilac-tinted photo behind the footer">
      <path d="M0 898C45 878 85 892 130 935C168 962 210 972 251 968V1049H0Z" fill="#caa9cd"/>
    </svg>
    <span class="footer__brand">PLUMVELLE</span>
    <p class="footer__tag">The best advisor<br>in the dating world</p>
    <div class="footer__rule"></div>
    <nav class="footer__links"><span>Contact</span><span>Terms of Use</span><span>Privacy Policy</span></nav>
    <p class="footer__url">PLUMVELLE.EXAMPLE</p>
  </footer>
</section>

</body>
</html>
```